TBNW site redesign

Please redesign a home page with content provided. PSD only - no coding
Can use any images from Vexelmarq.com

Please create a site design that more clearly illustrates the client's services and expertise. We are looking for a high-end design.

Any images used must be generic or of Dallas TX.

Fonts: Any
Colors: Match to logo
Look: Modern - Professional

Target Market(s)

medium-large business owners

Number of Pages Required

1 page

Font styles to use
Serif
Sans Serif

Requirements
Must have
• cohesive professional design
• high end look
• Match to logo

```html
<!DOCTYPE html>
<html lang="en">
<head>
<meta charset="utf-8">
<title>TBNW – Professional Office and Warehouse Leasing</title>
<link href="https://fonts.googleapis.com/css2?family=Tinos:wght@400;700&family=Open+Sans:wght@400;600;700&display=swap" rel="stylesheet">
<style>
:root{
  --red:#d52b2f;
  --red-dark:#b81f23;
  --ink:#222;
  --text:#555;
  --muted:#777;
  --light:#f3f3f3;
  --footer:#0c0c0c;
  --white:#fff;
  --serif:'Tinos', 'Times New Roman', serif;
  --sans:'Open Sans', Arial, sans-serif;
}
*{box-sizing:border-box;margin:0;padding:0}
html,body{width:1200px;height:4196px;overflow:hidden;background:var(--white)}
body{position:relative;font-family:var(--sans);color:var(--ink)}

/* header */
.site-header{position:absolute;left:0;top:0;width:1200px;height:140px;background:var(--white);border-top:6px solid var(--red);box-shadow:0 2px 8px rgba(0,0,0,.08);z-index:3}
.brand{position:absolute;left:92px;top:40px;display:flex;align-items:center;gap:12px}
.brand-square{width:30px;height:30px;background:var(--red)}
.brand-name{font-family:var(--serif);font-weight:400;font-size:34px;line-height:40px;color:var(--ink);letter-spacing:1px}
.phone{position:absolute;right:92px;top:32px;font-family:var(--sans);font-size:21px;color:var(--ink);display:flex;align-items:center;gap:10px}
.nav{position:absolute;right:92px;top:86px;display:flex;gap:36px;font-family:var(--sans);font-size:17px}
.nav a{color:var(--ink);text-decoration:none}
.nav a.active{color:var(--red)}

/* hero */
.hero{position:absolute;left:0;top:140px;width:1200px;height:620px;overflow:hidden}
.hero-photo{position:absolute;inset:0;background:linear-gradient(180deg,#e9eaea 0%,#d9dbdb 45%,#b9b4ac 75%,#8c7f6c 100%)}
.hero-panel{position:absolute;left:252px;top:106px;width:700px;height:170px;background:rgba(255,255,255,.82);border:2px solid rgba(255,255,255,.95);outline:1px solid rgba(0,0,0,.08);outline-offset:-12px;text-align:center;padding-top:30px}
.hero-panel h1{font-family:var(--serif);font-weight:700;font-size:24px;line-height:32px;color:var(--red);white-space:nowrap}
.hero-panel p{font-family:var(--serif);font-size:25px;line-height:38px;color:var(--ink);margin-top:4px}
.hero-arrows{position:absolute;left:104px;top:398px;display:flex;gap:6px}
.hero-arrows span{width:22px;height:22px;border-radius:50%;background:#333;display:flex;align-items:center;justify-content:center}
.hero-curve{position:absolute;left:0;top:520px}

/* why */
.section-title{position:absolute;left:0;width:1200px;text-align:center;font-family:var(--serif);font-weight:400;font-size:36px;color:var(--ink);letter-spacing:.5px}
.features{position:absolute;left:0;top:918px;width:1200px;height:270px}
.feature{position:absolute;width:260px;text-align:center}
.feature-icon{width:124px;height:124px;border-radius:50%;border:3px solid var(--red);margin:0 auto;display:flex;align-items:center;justify-content:center;box-shadow:0 4px 10px rgba(0,0,0,.15)}
.feature h3{font-family:var(--serif);font-weight:400;font-size:20px;margin-top:40px;color:var(--ink)}
.feature p{font-size:14px;line-height:22px;color:var(--text);margin-top:14px;padding:0 24px}
.intro{position:absolute;left:190px;top:1296px;width:820px;text-align:center;font-family:var(--serif);font-size:29px;line-height:54px;color:var(--ink)}
.btn{position:absolute;display:flex;align-items:center;justify-content:center;font-family:var(--serif);font-weight:700;font-size:19px;text-transform:uppercase;letter-spacing:.5px;white-space:nowrap}
.btn-red{left:470px;top:1432px;width:263px;height:54px;background:var(--red);color:var(--white);border-radius:3px}

/* team */
.team{position:absolute;left:0;top:1605px;width:1200px;height:627px;background:linear-gradient(180deg,rgba(213,43,47,.88),rgba(201,35,40,.92)),linear-gradient(90deg,#c54548,#e0a3a4 50%,#c54548)}
.team .section-title{color:var(--white);top:76px}
.team-card{position:absolute;top:179px;width:280px;height:356px;background:var(--white);text-align:center;box-shadow:0 4px 14px rgba(0,0,0,.25)}
.team-photo{width:180px;height:180px;border-radius:50%;margin:32px auto 0;border:4px solid #e6e6e6;background:linear-gradient(180deg,#d6d9dc,#6d7279)}
.team-card h3{font-family:var(--sans);font-weight:700;font-size:21px;margin-top:26px;color:var(--ink)}
.team-card p{font-size:15px;line-height:26px;color:var(--text);margin-top:8px;padding:0 26px}

/* testimonials */
.testimonial{position:absolute;left:92px;top:2573px;width:1018px;height:325px;background:#ececec;border-radius:10px;box-shadow:0 2px 10px rgba(0,0,0,.3);text-align:center}
.testimonial-photo{position:absolute;left:439px;top:-84px;width:140px;height:140px;border-radius:50%;border:4px solid var(--white);box-shadow:0 2px 8px rgba(0,0,0,.25);background:linear-gradient(180deg,#dcdcdc,#8d8580)}
.testimonial blockquote{position:absolute;left:90px;top:112px;width:838px;font-size:16px;line-height:30px;color:#333}
.q{color:var(--red);font-family:var(--serif);font-size:32px;line-height:0;vertical-align:-6px}
.testimonial cite{position:absolute;left:0;top:262px;width:100%;font-family:var(--sans);font-style:italic;color:var(--red);font-size:16px}
.slide-arrow{position:absolute;top:2722px}

/* articles */
.articles{position:absolute;left:0;top:3021px;width:1200px;height:629px;background:linear-gradient(180deg,#f7f7f7,#e9e9e9)}
.articles .section-title{top:91px}
.article-card{position:absolute;top:190px;width:310px;height:336px;background:var(--white);box-shadow:0 2px 8px rgba(0,0,0,.12);text-align:center}
.article-photo{height:168px;background:linear-gradient(180deg,#e7e9ea,#a9adb0)}
.article-date{display:inline-block;margin-top:-16px;position:relative;background:var(--red);color:var(--white);font-size:13px;line-height:28px;padding:0 26px}
.article-card h3{font-family:var(--serif);font-weight:400;font-size:19px;margin-top:18px;color:var(--ink)}
.article-card p{font-size:13px;line-height:20px;color:var(--text);margin-top:10px;padding:0 30px}
.read-more{display:block;font-size:12px;color:var(--red);margin-top:10px}

/* cta */
.cta{position:absolute;left:0;top:3650px;width:1200px;height:182px;background:var(--red)}
.cta p{position:absolute;left:123px;top:60px;font-family:var(--serif);font-size:25px;line-height:36px;color:var(--white);width:640px}
.btn-white{left:828px;top:64px;width:257px;height:52px;background:var(--white);color:var(--red);border-radius:3px}

/* footer */
.site-footer{position:absolute;left:0;top:3832px;width:1200px;height:364px;background:var(--footer);color:#ddd}
.footer-col{position:absolute;top:80px}
.footer-col h4{font-family:var(--serif);font-size:14px;font-weight:400;letter-spacing:.5px;text-transform:uppercase;color:#eee;margin-bottom:20px}
.footer-col li{list-style:none;font-size:13px;line-height:26px;display:flex;align-items:flex-start;gap:10px}
.contact li{margin-bottom:8px;line-height:22px}
.ico{flex:0 0 24px;height:24px;border-radius:50%;border:1.5px solid #ddd;display:flex;align-items:center;justify-content:center;margin-top:-1px}
.copyright{position:absolute;left:0;top:296px;width:1200px;text-align:center;font-size:13px;color:#ddd}
</style>
</head>
<body>

<header class="site-header">
  <div class="brand">
    <span class="brand-square"></span>
    <span class="brand-name">TBNW</span>
  </div>
  <div class="phone">
    <svg width="20" height="20" viewBox="0 0 24 24"><path fill="#d52b2f" d="M6.6 10.8a15.1 15.1 0 0 0 6.6 6.6l2.2-2.2c.3-.3.7-.4 1-.2 1.1.4 2.3.6 3.6.6.6 0 1 .4 1 1V20c0 .6-.4 1-1 1A17 17 0 0 1 3 4c0-.6.4-1 1-1h3.5c.6 0 1 .4 1 1 0 1.3.2 2.5.6 3.6.1.3 0 .7-.2 1z"/></svg>
    Call Today: 214-555-0142
  </div>
  <nav class="nav">
    <a class="active" href="#">Home</a><a href="#">Services</a><a href="#">About tbnw</a><a href="#">Contact us</a><a href="#">Blog</a><a href="#">Market news</a>
  </nav>
</header>

<section class="hero">
  <div class="hero-photo" role="img" aria-label="Bright open-plan office with white desks, computers and large windows"></div>
  <div class="hero-panel">
    <h1>PROFESSIONAL OFFICE AND WAREHOUSE LEASING</h1>
    <p>Fast-track your search with tenant reps that only<br>serve you, and specialize in the DFW area.</p>
  </div>
  <div class="hero-arrows">
    <span><svg width="10" height="10" viewBox="0 0 10 10"><path d="M7 1 3 5l4 4" fill="none" stroke="#fff" stroke-width="2"/></svg></span>
    <span><svg width="10" height="10" viewBox="0 0 10 10"><path d="M3 1l4 4-4 4" fill="none" stroke="#fff" stroke-width="2"/></svg></span>
  </div>
  <svg class="hero-curve" width="1200" height="100" viewBox="0 0 1200 100">
    <path d="M0 40 Q600 140 1200 40 L1200 100 L0 100Z" fill="#fff"/>
    <path d="M230 68 Q600 -10 980 70 Q600 20 230 68Z" fill="#d52b2f"/>
  </svg>
</section>

<h2 class="section-title" style="top:806px">WHY TENANT REPRESENTATION?</h2>
<div class="features">
  <div class="feature" style="left:74px">
    <div class="feature-icon"><svg width="52" height="44" viewBox="0 0 52 44" fill="#d52b2f"><circle cx="26" cy="10" r="8"/><path d="M12 38c0-9 6-15 14-15s14 6 14 15z"/><circle cx="9" cy="15" r="6"/><path d="M0 36c0-7 4-11 9-11 2 0 4 1 5 2-2 3-3 6-3 9z"/><circle cx="43" cy="15" r="6"/><path d="M52 36c0-7-4-11-9-11-2 0-4 1-5 2 2 3 3 6 3 9z"/></svg></div>
    <h3>Relationships</h3>
    <p>Save time by trusting TBNW year after year to find the right location for you.</p>
  </div>
  <div class="feature" style="left:348px">
    <div class="feature-icon"><svg width="46" height="46" viewBox="0 0 46 46" fill="none" stroke="#d52b2f" stroke-width="4"><path d="M30 8H8v30h30V18"/><path d="M20 27l2-7L38 4l5 5-16 16z" fill="#d52b2f"/></svg></div>
    <h3>Access to More</h3>
    <p>We have no agreements or personal incentives for specific properties, so we can</p>
  </div>
  <div class="feature" style="left:620px">
    <div class="feature-icon"><svg width="48" height="44" viewBox="0 0 48 44" fill="#d52b2f"><path d="M2 20 46 2 38 40 26 30 20 42 18 28 40 8 14 25z"/></svg></div>
    <h3>Free To You</h3>
    <p>You pay us nothing. We get our commission from the property being leased.</p>
  </div>
  <div class="feature" style="left:888px">
    <div class="feature-icon"><svg width="50" height="44" viewBox="0 0 50 44"><rect x="2" y="2" width="46" height="30" rx="2" fill="#d52b2f"/><rect x="7" y="7" width="36" height="18" fill="#fff"/><rect x="20" y="32" width="10" height="6" fill="#d52b2f"/><rect x="13" y="38" width="24" height="4" fill="#d52b2f"/></svg></div>
    <h3>Customized Service</h3>
    <p>Aside from saving you the time of repeating what your needs are to each new</p>
  </div>
</div>

<p class="intro">If you need to find office or warehouse space in the Dallas Fort Worth area, the team at TBNW has the experience you need.</p>
<div class="btn btn-red">Space Calculator</div>

<section class="team" role="img" aria-label="Red-tinted view of a modern office interior behind the team cards">
  <h2 class="section-title">OUR TEAM</h2>
  <div class="team-card" style="left:140px">
    <div class="team-photo" role="img" aria-label="Portrait of the founder"></div>
    <h3>Owen R. Brennan</h3>
    <p>Founder and President</p>
  </div>
  <div class="team-card" style="left:459px">
    <div class="team-photo" role="img" aria-label="Portrait of the senior director"></div>
    <h3>Dale Hart-Summers,</h3>
    <p>Senior Director, Commercial Property Specialist</p>
  </div>
  <div class="team-card" style="left:778px">
    <div class="team-photo" role="img" aria-label="Portrait of the associate"></div>
    <h3>Lucas Andrew Fenwick</h3>
    <p>Jr., Associate, Tenant Rep Specialist</p>
  </div>
</section>

<h2 class="section-title" style="top:2428px">CLIENT TESTIMONIALS</h2>
<div class="testimonial">
  <div class="testimonial-photo" role="img" aria-label="Portrait of the client"></div>
  <blockquote><span class="q">“</span>The real estate team at TBNW has decades of experience in Commercial. One advantage of TBNW is they know all the properties that are about to become available, BEFORE they are available. They have the inside track on properties and they watch your back at the negotiating table. Very impressive with a polished approach. Let the team run with your next project and you won’t be disappointed.<span class="q">”</span></blockquote>
  <cite>-Nathaniel James Corbin</cite>
</div>
<svg class="slide-arrow" style="left:92px" width="24" height="30" viewBox="0 0 24 30"><path d="M16 4 6 15l10 11" fill="none" stroke="#555" stroke-width="2.5"/></svg>
<svg class="slide-arrow" style="left:1086px" width="24" height="30" viewBox="0 0 24 30"><path d="M8 4l10 11-10 11" fill="none" stroke="#555" stroke-width="2.5"/></svg>

<section class="articles">
  <h2 class="section-title">RECENT ARTICLES</h2>
  <article class="article-card" style="left:109px">
    <div class="article-photo" role="img" aria-label="Glass-walled office interior"></div>
    <span class="article-date">14th May 2018</span>
    <h3>Neque porro quisquam</h3>
    <p>The point of using Lorem Ipsum is that it has a more-or-less normal distribution</p>
    <span class="read-more">Read More »</span>
  </article>
  <article class="article-card" style="left:445px">
    <div class="article-photo" style="background:linear-gradient(180deg,#cfd3d6,#6f757a)" role="img" aria-label="Empty warehouse interior"></div>
    <span class="article-date">14th May 2018</span>
    <h3>Porro quisquam est</h3>
    <p>The point of using Lorem Ipsum is that it has a more-or-less normal distribution</p>
    <span class="read-more">Read More »</span>
  </article>
  <article class="article-card" style="left:783px">
    <div class="article-photo" style="background:linear-gradient(180deg,#e3e4e4,#8b8780)" role="img" aria-label="Open-plan office with workstations"></div>
    <span class="article-date">14th May 2018</span>
    <h3>Dolorem ipsum quia</h3>
    <p>The point of using Lorem Ipsum is that it has a more-or-less normal distribution</p>
    <span class="read-more">Read More »</span>
  </article>
</section>

<section class="cta">
  <p>Whether your lease is expiring soon, or you’re just starting your search, TBNW can help you find the perfect space.</p>
  <div class="btn btn-white">Make an Appointment</div>
</section>

<footer class="site-footer">
  <div class="footer-col" style="left:92px">
    <h4>Information</h4>
    <ul><li>› Privacy Policy</li><li>› Meet our providers</li><li>› About us</li><li>› Cookies Policy</li></ul>
  </div>
  <div class="footer-col contact" style="left:338px">
    <h4>Contact us</h4>
    <ul>
      <li><span class="ico"><svg width="10" height="12" viewBox="0 0 10 12"><path d="M5 0a4 4 0 0 0-4 4c0 3 4 8 4 8s4-5 4-8a4 4 0 0 0-4-4z" fill="#ddd"/></svg></span>410 Cedar Row Avenue, Suite 300,<br>Dallas, TX 75201</li>
      <li><span class="ico"><svg width="11" height="11" viewBox="0 0 24 24"><path fill="#ddd" d="M6.6 10.8a15.1 15.1 0 0 0 6.6 6.6l2.2-2.2c.3-.3.7-.4 1-.2 1.1.4 2.3.6 3.6.6.6 0 1 .4 1 1V20c0 .6-.4 1-1 1A17 17 0 0 1 3 4c0-.6.4-1 1-1h3.5c.6 0 1 .4 1 1 0 1.3.2 2.5.6 3.6.1.3 0 .7-.2 1z"/></svg></span>214-555-0142 | Fax: 214-555-0178</li>
      <li><span class="ico"><svg width="11" height="9" viewBox="0 0 12 9"><rect x=".5" y=".5" width="11" height="8" fill="none" stroke="#ddd"/><path d="M.5.5 6 5l5.5-4.5" fill="none" stroke="#ddd"/></svg></span>info@examplemail.com</li>
    </ul>
  </div>
  <div class="footer-col" style="left:666px">
    <h4>State Realty Licensing Board Mandated Disclosure Notices</h4>
    <ul><li>› State Realty Licensing Board Information About Brokerage Services</li><li>› State Realty Licensing Board Consumer Protection Notice</li></ul>
  </div>
  <div class="copyright">Copyright © 2018. All Rights Reserved</div>
</footer>

</body>
</html>
```